El Tallercito Brochure

Create a brochure for a new reception venue - El Tallercito
www.El-Tallercito-Salon.com

Here is info it must contain

Please refer to our site for inspiration - I know this is alot of info but ?

El Tallercito Reception Hall
4178C Millbrook Rd, Maplecrest, CA 707-555-0148
www.El-Tallercito-Salon.com

Located in Maplecrest, California, we are a new venue that can host a variety of events. We can provide an exceptional space for your next party, reception, quinceañera, birthday party, or meeting! We treat each client with respect and go out of our way to accommodate all of your needs and make your event a success. Conveniently located just off the Route 41/47 junction, El Tallercito is located in a safe, well-lit area with a large private parking area.

The space comes prepared with everything you need to get your party started – chairs and tables with tablecloths, a well-equipped kitchen, and incredible decorations to set the perfect backdrop to your event! Rent just the Lounge for a more intimate get-together, or add the Main Hall for your large sit-down event.

Lounge – Beautiful 1,600 ft2 entry room featuring large living room with conversation sofa seating for 40+ Sound system  Pass-through bar with seating  Fully-equipped 200 ft2 kitchen with
4-burner gas stove, oven, large double sink, full-size refrigerator, 2 microwaves, and ice machine, plus lots of storage and counter space  Newly-remodeled Men’s and Women’s bathrooms

Main Hall – Spacious 24’x80’ room with seating for up to 160 people  2,000 ft2  72” round tables with chairs, each seating up to 8 guests  DJ stand and Sound system  Atmospheric lighting
_______________________________________
Pricing -
Daytime Parties
Available 8AM-2PM
4-hour minimum

Lounge and Kitchen Only
Fri - Sat - Sun : $80/hr
Mon - Thurs : $60/hr

All Areas: Lounge, Kitchen, Main Hall, and Backyard
Fri - Sat - Sun : $120/hr
Mon - Thurs : $100/hr
___________________________________________
Evening Events
Available 3PM-12AM
5-hour minimum

Lounge and Kitchen Only -
Fri - Sat - Sun : $100/hr
Mon - Thurs : $50/hr

Fri - Sat - Sun : $160/hr
Mon - Thurs : $75/hr
___________________________________________________
Looking for a different time frame, all-day rental, or other special request? Let us know!
We'd be happy to provide you with a custom quote for your event.

```html
<!DOCTYPE html>
<html lang="en">
<head>
<meta charset="utf-8">
<title>El Tallercito Brochure</title>
<link href="https://fonts.googleapis.com/css2?family=Open+Sans:wght@400;600;700&family=Raleway:wght@400;500;600&display=swap" rel="stylesheet">
<style>
  :root {
    --page-bg: #d9d7d3;
    --panel: #ececee;
    --panel-shade: #dcdcdf;
    --orange: #e8922a;
    --orange-deep: #c9711a;
    --ink: #3b3834;
    --ink-soft: #5e5a55;
    --heading: #6d6b68;
    --photo-warm-1: #6e5a45;
    --photo-warm-2: #b89a78;
    --photo-dark-1: #1f1a16;
    --photo-dark-2: #5a4632;
  }
  * { box-sizing: border-box; margin: 0; padding: 0; }
  html, body { width: 1200px; height: 2468px; overflow: hidden; }
  body {
    background: var(--page-bg);
    font-family: "Open Sans", Arial, sans-serif;
    color: var(--ink);
    position: relative;
  }
  .spread {
    position: absolute;
    left: 50px;
    width: 1100px;
    height: 850px;
    background: linear-gradient(180deg, var(--panel) 0%, var(--panel-shade) 100%);
    box-shadow: 0 6px 20px rgba(0,0,0,.18);
    overflow: hidden;
  }
  .spread--inside { top: 309px; }
  .spread--outside { top: 1309px; }
  .panels {
    position: absolute; inset: 0;
    display: grid;
    grid-template-columns: repeat(3, 1fr);
  }
  .panel { position: relative; padding: 34px 30px; border-right: 1px solid rgba(0,0,0,.06); }
  .panel:last-child { border-right: none; }
  .panel-title {
    font-family: "Raleway", "Open Sans", sans-serif;
    font-weight: 500;
    font-size: 25px;
    color: var(--heading);
    margin-bottom: 12px;
    letter-spacing: .3px;
  }
  .body-text { font-size: 10.5px; line-height: 1.5; color: var(--ink); margin-bottom: 9px; }
  .body-text strong { font-weight: 700; }
  .photo { border-radius: 2px; }
  .photo--warm { background: linear-gradient(135deg, var(--photo-warm-1), var(--photo-warm-2)); }
  .photo--dark { background: radial-gradient(circle at 60% 35%, var(--photo-dark-2), var(--photo-dark-1) 75%); }

  /* Inside spread */
  .pricing-cols { display: grid; grid-template-columns: 1fr 1fr; gap: 16px; }
  .pricing-head { font-size: 12px; font-weight: 700; color: var(--ink); margin-bottom: 2px; }
  .pricing-note { font-size: 10px; color: var(--ink-soft); line-height: 1.45; margin-bottom: 10px; }
  .rate-group { margin-bottom: 12px; }
  .rate-label { font-size: 10px; font-weight: 600; line-height: 1.4; margin-bottom: 3px; }
  .rate-line { font-size: 10px; line-height: 1.5; color: var(--ink-soft); }
  .pricing-footer { font-size: 10.5px; line-height: 1.5; text-align: center; margin-top: 8px; color: var(--ink); }
  .venue-row { display: grid; grid-template-columns: 120px 1fr; gap: 14px; margin-bottom: 22px; align-items: start; }
  .venue-row .photo { height: 78px; border: 3px solid #fff; box-shadow: 0 1px 3px rgba(0,0,0,.25); }
  .venue-name { font-size: 11.5px; font-weight: 700; margin-bottom: 3px; }
  .venue-desc { font-size: 10px; line-height: 1.45; color: var(--ink-soft); }
  .panorama {
    position: absolute; left: 0; right: 0; bottom: 0; height: 300px;
    background: linear-gradient(180deg, #8c7a66 0%, #a48d72 35%, #5d4a39 70%, #3e3126 100%);
  }
  .wave { position: absolute; left: 0; top: 500px; width: 1100px; height: 130px; }

  /* Outside spread */
  .flap-row { display: grid; grid-template-columns: 96px 1fr; gap: 14px; margin-bottom: 20px; }
  .flap-row .photo { height: 72px; border: 3px solid #fff; box-shadow: 0 1px 3px rgba(0,0,0,.25); }
  .contact-list { list-style: none; font-size: 11px; line-height: 1.7; margin: 10px 0 14px; }
  .contact-list li { display: flex; align-items: center; gap: 8px; }
  .contact-list svg { width: 12px; height: 12px; flex: none; }
  .back-photo-small { height: 120px; margin-bottom: 14px; }
  .back-photo-large { height: 220px; margin-top: 6px; }
  .cover { padding: 0; }
  .cover-photo {
    position: absolute; left: 0; right: 0; top: 0; height: 620px;
    background: radial-gradient(circle at 55% 25%, #8a6a44 0%, #3a2c1f 55%, #1d1711 100%);
  }
  .cover-wave { position: absolute; left: 0; top: 560px; width: 367px; height: 70px; }
  .cover-name {
    position: absolute; right: 34px; bottom: 78px;
    font-family: "Open Sans", Arial, sans-serif;
    font-weight: 600; font-size: 30px; color: var(--ink);
  }
  .cover-web {
    position: absolute; right: 34px; bottom: 52px;
    font-size: 11px; color: var(--ink-soft);
  }
</style>
</head>
<body>

<section class="spread spread--inside" aria-label="Brochure inside spread">
  <div class="panorama" role="img" aria-label="Panoramic photo of the lounge with sofas, tables and large windows"></div>
  <svg class="wave" viewBox="0 0 1100 130" preserveAspectRatio="none" aria-hidden="true">
    <path d="M0,0 H1100 V40 C820,100 560,10 300,40 C180,55 80,80 0,95 Z" fill="#e4e4e7"/>
    <path d="M0,95 C80,80 180,55 300,40 C560,10 820,100 1100,40 V62 C820,122 560,32 300,62 C180,77 80,102 0,117 Z" fill="var(--orange)"/>
    <path d="M0,117 C80,102 180,77 300,62 C560,32 820,122 1100,62 V70 C820,130 560,40 300,70 C180,85 80,110 0,125 Z" fill="var(--orange-deep)"/>
  </svg>
  <div class="panels">
    <div class="panel panel--about">
      <h2 class="panel-title">About the Venue</h2>
      <p class="body-text">Located in Maplecrest, California, we are a new venue that can host a variety of events. We can provide an exceptional space for your next party, reception, quinceañera, birthday party, or meeting! We treat each client with respect and go out of our way to accommodate all of your needs. Conveniently located just off the Route 41/47 junction, in a safe, well-lit area with a large private parking area.</p>
      <p class="body-text"><strong>Lounge</strong> – Beautiful 1,600 ft² entry room with conversation sofa seating for 40+, sound system, pass-through bar with seating, fully-equipped 200 ft² kitchen, and newly-remodeled bathrooms.</p>
      <p class="body-text"><strong>Main Hall</strong> – Spacious 24’x80’ room with seating for up to 160 people, 72” round tables with chairs, DJ stand, sound system and atmospheric lighting.</p>
    </div>
    <div class="panel panel--pricing">
      <h2 class="panel-title">Pricing</h2>
      <div class="pricing-cols">
        <div>
          <p class="pricing-head">Daytime Parties</p>
          <p class="pricing-note">Available 8AM-2PM<br>4-hour minimum</p>
          <div class="rate-group">
            <p class="rate-label">Lounge and Kitchen Only</p>
            <p class="rate-line">Fri - Sat - Sun : $80/hr</p>
            <p class="rate-line">Mon - Thurs : $60/hr</p>
          </div>
          <div class="rate-group">
            <p class="rate-label">All Areas</p>
            <p class="rate-line">Fri - Sat - Sun : $120/hr</p>
            <p class="rate-line">Mon - Thurs : $100/hr</p>
          </div>
        </div>
        <div>
          <p class="pricing-head">Evening Events</p>
          <p class="pricing-note">Available 3PM-12AM<br>5-hour minimum</p>
          <div class="rate-group">
            <p class="rate-label">Lounge and Kitchen Only</p>
            <p class="rate-line">Fri - Sat - Sun : $100/hr</p>
            <p class="rate-line">Mon - Thurs : $50/hr</p>
          </div>
          <div class="rate-group">
            <p class="rate-label">All Areas</p>
            <p class="rate-line">Fri - Sat - Sun : $160/hr</p>
            <p class="rate-line">Mon - Thurs : $75/hr</p>
          </div>
        </div>
      </div>
      <p class="pricing-footer">Looking for a different time frame, all-day rental, or other special request? Let us know! We'd be happy to provide a custom quote.</p>
    </div>
    <div class="panel panel--venue">
      <h2 class="panel-title">Our Venue</h2>
      <div class="venue-row">
        <div class="photo photo--warm" role="img" aria-label="Photo of the lounge sofa seating"></div>
        <div><p class="venue-name">Lounge</p><p class="venue-desc">1,600 ft² entry room with sofa seating for 40+ and a pass-through bar.</p></div>
      </div>
      <div class="venue-row">
        <div class="photo photo--warm" role="img" aria-label="Photo of the main hall with round tables"></div>
        <div><p class="venue-name">Main Hall</p><p class="venue-desc">2,000 ft² room seating up to 160 guests at 72” round tables.</p></div>
      </div>
      <div class="venue-row">
        <div class="photo photo--warm" role="img" aria-label="Photo of the equipped kitchen"></div>
        <div><p class="venue-name">Kitchen</p><p class="venue-desc">Gas stove, oven, double sink, refrigerator, microwaves and ice machine.</p></div>
      </div>
    </div>
  </div>
</section>

<section class="spread spread--outside" aria-label="Brochure outside spread">
  <div class="panels">
    <div class="panel panel--flap">
      <h2 class="panel-title">Your Event</h2>
      <div class="flap-row">
        <div class="photo photo--dark" role="img" aria-label="Photo of a party set up at the venue"></div>
        <div><p class="venue-name">Parties</p><p class="venue-desc">Birthdays and get-togethers in the Lounge or Main Hall.</p></div>
      </div>
      <div class="flap-row">
        <div class="photo photo--dark" role="img" aria-label="Photo of a reception table setting"></div>
        <div><p class="venue-name">Receptions</p><p class="venue-desc">Large sit-down events with seating for up to 160.</p></div>
      </div>
      <div class="flap-row">
        <div class="photo photo--dark" role="img" aria-label="Photo of decorated hall with lighting"></div>
        <div><p class="venue-name">Quinceañeras</p><p class="venue-desc">Incredible decorations and atmospheric lighting.</p></div>
      </div>
      <div class="flap-row">
        <div class="photo photo--dark" role="img" aria-label="Photo of the lounge set for a meeting"></div>
        <div><p class="venue-name">Meetings</p><p class="venue-desc">An intimate Lounge with sound system and bar.</p></div>
      </div>
    </div>
    <div class="panel panel--back">
      <div class="photo photo--warm back-photo-small" role="img" aria-label="Photo of the venue entrance"></div>
      <h2 class="panel-title">Contact Us</h2>
      <p class="body-text">The space comes prepared with everything you need – chairs and tables with tablecloths, a well-equipped kitchen, and incredible decorations to set the perfect backdrop to your event!</p>
      <ul class="contact-list">
        <li><svg viewBox="0 0 12 12" aria-hidden="true"><path d="M6 0.5a3.6 3.6 0 0 0-3.6 3.6C2.4 7 6 11.5 6 11.5S9.6 7 9.6 4.1A3.6 3.6 0 0 0 6 .5zm0 5a1.4 1.4 0 1 1 0-2.8 1.4 1.4 0 0 1 0 2.8z" fill="var(--orange)"/></svg>4178C Millbrook Rd, Maplecrest, CA</li>
        <li><svg viewBox="0 0 12 12" aria-hidden="true"><path d="M2.6 0.8 L4.2 3.2 L3.2 4.4 C3.9 5.9 5.1 7.1 6.6 7.8 L7.8 6.8 L10.2 8.4 L9.4 10.4 C5.6 10.4 1.6 6.4 1.6 2.6 Z" fill="var(--orange)"/></svg>707-555-0148</li>
        <li><svg viewBox="0 0 12 12" aria-hidden="true"><circle cx="6" cy="6" r="5" fill="none" stroke="var(--orange)" stroke-width="1.3"/><path d="M1 6h10M6 1c2 2.5 2 7.5 0 10M6 1c-2 2.5-2 7.5 0 10" fill="none" stroke="var(--orange)" stroke-width="1"/></svg>www.El-Tallercito-Salon.com</li>
      </ul>
      <div class="photo photo--dark back-photo-large" role="img" aria-label="Photo of hanging globe lights in the hall"></div>
    </div>
    <div class="panel cover">
      <div class="cover-photo" role="img" aria-label="Photo of the reception hall interior with hanging lights"></div>
      <svg class="cover-wave" viewBox="0 0 366 70" preserveAspectRatio="none" aria-hidden="true">
        <path d="M0,60 C120,10 240,10 366,40 V70 H0 Z" fill="var(--panel)"/>
        <path d="M0,60 C120,10 240,10 366,40 V56 C240,26 120,26 0,70 Z" fill="var(--orange)"/>
      </svg>
      <p class="cover-name">El Tallercito</p>
      <p class="cover-web">www.El-Tallercito-Salon.com</p>
    </div>
  </div>
</section>

</body>
</html>
```